Long term design collaboration - mobile app design & web app design

We are looking for a talented mobile designer to help us improve our UI & UX for mobile app and web app.

The screens that need to be redesigned are attached.

There is potentially a lot more work in future design available for the successful candidate.
The successful candidate would have to take part in daily stand-up around 3 times per week.
The successful candidate would join a dev team
We are software company that does property management

```html
<!DOCTYPE html>
<html lang="en">
<head>
<meta charset="utf-8">
<title>Tenvale – Overview</title>
<link href="https://fonts.googleapis.com/css2?family=Inter:wght@400;500;600;700&display=swap" rel="stylesheet">
<style>
:root{
  --bg:#f3f3f3;
  --panel:#ffffff;
  --ink:#111111;
  --muted:#666666;
  --line:#e3e3e3;
  --blue:#2457c5;
  --blue-soft:#eef5fd;
  --teal:#4db6a0;
  --teal-soft:#f0faf7;
  --teal-line:#9adccc;
  --red:#d9443b;
  --red-ink:#c62828;
  --orange-ink:#c2410c;
  --card:#f7f7f7;
  --tag:#ececec;
}
*{box-sizing:border-box;margin:0;padding:0}
html,body{width:980px;height:1200px;overflow:hidden;background:var(--bg)}
body{font-family:'Inter',sans-serif;color:var(--ink)}
.stage{position:absolute;left:0;top:0;width:1736px;height:2126px;transform:scale(0.56452);transform-origin:0 0}
.abs{position:absolute}
svg{display:block}

/* sidebar */
.sidebar{left:39px;top:39px;width:337px;height:2048px;background:var(--panel);border-radius:20px}
.brand{left:19px;top:24px;font-size:30px;font-weight:700}
.close-btn{left:274px;top:19px;width:44px;height:44px;border:1px solid var(--line);border-radius:8px;display:flex;align-items:center;justify-content:center;box-shadow:0 2px 3px rgba(0,0,0,.06)}
.nav-label{left:19px;font-size:15px;letter-spacing:1px;color:var(--muted);font-weight:500}
.nav-item{left:19px;width:299px;height:48px;display:flex;align-items:center;padding-left:12px;gap:12px;font-size:20px;border-radius:8px}
.nav-item.active{background:var(--blue);color:#fff}
.nav-item .chev{position:absolute;right:12px}
.badge{position:absolute;right:10px;width:29px;height:28px;border-radius:5px;background:var(--red);color:#fff;font-size:15px;font-weight:600;display:flex;align-items:center;justify-content:center}
.logout{left:19px;top:1986px;width:299px;height:46px;display:flex;align-items:center;gap:14px;font-size:20px}
.logout .go{position:absolute;right:0;width:38px;height:38px;border:1px solid #999;border-radius:8px;display:flex;align-items:center;justify-content:center}

/* top bar */
.topbar{left:396px;top:39px;width:1301px;height:86px;background:var(--panel);border-radius:20px}
.back-btn{left:19px;top:19px;width:94px;height:48px;border:1px solid var(--line);border-radius:10px;display:flex;align-items:center;justify-content:center;gap:8px;font-size:18px;font-weight:600;box-shadow:0 2px 3px rgba(0,0,0,.06)}
.crumbs{left:132px;top:31px;display:flex;align-items:center;gap:14px;font-size:18px;color:var(--muted)}
.crumbs .here{color:var(--ink);font-weight:600}
.bell-btn{left:935px;top:19px;width:48px;height:48px;border:1px solid var(--line);border-radius:10px;display:flex;align-items:center;justify-content:center;box-shadow:0 2px 3px rgba(0,0,0,.06)}
.avatar{left:1012px;top:19px;width:47px;height:47px;border-radius:8px;background:linear-gradient(135deg,#3a3a3a,#8a8a8a)}
.user-name{left:1070px;top:21px;font-size:20px;font-weight:600}
.user-role{left:1070px;top:48px;font-size:15px;color:var(--muted)}
.user-chev{left:1258px;top:34px}

/* main */
.main{left:396px;top:145px;width:1301px;height:1942px;background:var(--panel);border-radius:20px}
.title{left:19px;top:22px;font-size:31px;font-weight:700}
.desc{left:19px;top:68px;width:1020px;font-size:17px;line-height:24px;color:var(--muted)}
.report-btn{left:1106px;top:38px;width:176px;height:58px;background:var(--blue);color:#fff;border-radius:8px;font-size:20px;font-weight:700;display:flex;align-items:center;justify-content:center}
.updated{left:19px;top:135px;width:1263px;height:62px;background:var(--blue-soft);border-radius:14px;font-size:18px;display:flex;align-items:center;padding-left:19px}
.setup{left:19px;top:217px;width:1263px;height:293px;background:var(--teal-soft);border:1.5px solid var(--teal-line);border-radius:6px}
.setup h2{position:absolute;left:18px;top:20px;font-size:23px;font-weight:700}
.setup-row{position:absolute;left:18px;width:1225px;height:46px;display:flex;align-items:center;font-size:23px;font-weight:500}
.setup-row .dot{width:24px;height:24px;border-radius:50%;background:var(--teal);margin-right:10px}
.setup-row .btn{position:absolute;right:0;width:130px;height:46px;background:#fff;border:1.5px solid var(--teal-line);border-radius:8px;display:flex;align-items:center;justify-content:center;gap:10px;font-size:21px;font-weight:400}
.divider{left:19px;top:538px;width:1263px;height:1px;background:var(--line)}
.tabs{left:19px;top:567px;width:1263px;height:63px;background:#f5f5f5;border-radius:8px}
.tab{position:absolute;top:4px;height:54px;width:627px;display:flex;align-items:center;justify-content:center;font-size:22px;font-weight:700}
.tab.on{left:5px;background:#fff;color:var(--blue);border-radius:6px;box-shadow:0 2px 4px rgba(0,0,0,.1)}
.tab.off{left:631px}
.section-h{left:19px;font-size:23px;font-weight:700}
.table{left:19px;top:712px;width:1263px;height:328px;border:1.5px solid var(--line);border-radius:6px}
.trow{position:absolute;left:0;width:100%;height:82px;display:flex;align-items:center;border-bottom:1.5px solid var(--line)}
.trow:last-child{border-bottom:none}
.trow .k{position:absolute;left:18px;font-size:20px;font-weight:700}
.trow .v{position:absolute;left:312px;font-size:20px;color:#555}
.trow .go{position:absolute;right:18px;width:48px;height:48px;border:1.5px solid var(--line);border-radius:8px;display:flex;align-items:center;justify-content:center;box-shadow:0 2px 3px rgba(0,0,0,.06)}
.tile{width:240px;height:144px;background:var(--card);border-radius:8px}
.tile .tag{position:absolute;left:9px;top:10px;height:34px;padding:0 10px;border-radius:6px;background:var(--tag);font-size:20px;display:flex;align-items:center}
.tile .ico{position:absolute;right:12px;top:14px}
.tile .box{position:absolute;left:9px;top:58px;right:9px;height:82px;background:#fff;border-radius:6px;box-shadow:0 2px 4px rgba(0,0,0,.1);padding:12px 12px 0;font-size:17px;line-height:36px}
.tile .box .sub{font-size:15px;line-height:34px}
.tile.warn{background:#fff6ef}
.tile.warn .tag{background:#fde6d6;color:var(--orange-ink)}
.tile.alert{background:#fdeeee}
.tile.alert .tag{background:#fbdada;color:var(--red-ink)}
.tile.alert .box .first{color:var(--red-ink)}
.tile.wide{width:248px}
</style>
</head>
<body>
<div class="stage">

  <aside class="sidebar abs">
    <div class="brand abs">Tenvale</div>
    <div class="close-btn abs"><svg width="18" height="18" viewBox="0 0 18 18"><path d="M3 3l12 12M15 3L3 15" stroke="#111" stroke-width="2" stroke-linecap="round"/></svg></div>

    <div class="nav-label abs" style="top:87px">OVERVIEW</div>
    <div class="nav-item active abs" style="top:115px"><svg width="24" height="24" viewBox="0 0 24 24" fill="none" stroke="#fff" stroke-width="2"><path d="M4 10l8-6 8 6v10H4z"/><path d="M10 20v-5h4v5"/></svg>Home</div>
    <div class="nav-item abs" style="top:168px"><svg width="24" height="24" viewBox="0 0 24 24" fill="none" stroke="#111" stroke-width="2"><path d="M3 10v4h4l7 4V6l-7 4z"/><path d="M18 9l3-2M18 15l3 2M19 12h3"/></svg>Announcements</div>
    <div class="nav-item abs" style="top:221px"><svg width="24" height="24" viewBox="0 0 24 24" fill="none" stroke="#111" stroke-width="2"><path d="M6 17V11a6 6 0 0112 0v6l2 2H4z"/><path d="M10 21h4"/></svg>Notifications<span class="badge">2</span></div>
    <div class="nav-item abs" style="top:274px"><svg width="24" height="24" viewBox="0 0 24 24" fill="none" stroke="#111" stroke-width="2"><rect x="3" y="5" width="18" height="14" rx="1"/><path d="M3 6l9 7 9-7"/></svg>Messages<span class="badge">9</span></div>

    <div class="nav-label abs" style="top:348px">FINANCIAL</div>
    <div class="nav-item abs" style="top:376px"><svg width="24" height="24" viewBox="0 0 24 24" fill="none" stroke="#111" stroke-width="2"><path d="M3 9l9-5 9 5zM5 10v8M10 10v8M14 10v8M19 10v8M3 20h18"/></svg>Bank Balance<svg class="chev" width="16" height="16" viewBox="0 0 16 16"><path d="M4 6l4 4 4-4" stroke="#111" stroke-width="2" fill="none"/></svg></div>
    <div class="nav-item abs" style="top:429px"><svg width="24" height="24" viewBox="0 0 24 24" fill="none" stroke="#111" stroke-width="2"><path d="M6 3h12v18l-3-2-3 2-3-2-3 2zM9 8h6M9 12h6"/></svg>Billing</div>
    <div class="nav-item abs" style="top:482px"><svg width="24" height="24" viewBox="0 0 24 24" fill="none" stroke="#111" stroke-width="2"><rect x="3" y="3" width="18" height="18" rx="1"/><path d="M8 8h1M12 8h1M16 8h1M8 12h1M12 12h1M16 12h1M8 16h1M12 16h1M16 16h1"/></svg>Ground Rent</div>
    <div class="nav-item abs" style="top:535px"><svg width="24" height="24" viewBox="0 0 24 24" fill="none" stroke="#111" stroke-width="2"><path d="M6 3h9l4 4v14H6z"/><path d="M12 9v8M14 10h-3a1.5 1.5 0 000 3h2a1.5 1.5 0 010 3h-3"/></svg>Property Balance<svg class="chev" width="16" height="16" viewBox="0 0 16 16"><path d="M4 6l4 4 4-4" stroke="#111" stroke-width="2" fill="none"/></svg></div>
    <div class="nav-item abs" style="top:588px"><svg width="24" height="24" viewBox="0 0 24 24" fill="none" stroke="#111" stroke-width="2"><path d="M6 3h9l4 4v14H6z"/><path d="M9 17l6-6M9 11h1M14 17h1"/></svg>Service Charge</div>

    <div class="nav-label abs" style="top:662px">MANAGEMENT &amp; RESOURCES</div>
    <div class="nav-item abs" style="top:689px"><svg width="24" height="24" viewBox="0 0 24 24" fill="none" stroke="#111" stroke-width="2"><rect x="3" y="3" width="18" height="18" rx="1"/><path d="M10 9l-3 3 3 3M14 9l3 3-3 3"/></svg>Development Parameters</div>
    <div class="nav-item abs" style="top:742px"><svg width="24" height="24" viewBox="0 0 24 24" fill="none" stroke="#111" stroke-width="2"><ellipse cx="12" cy="6" rx="8" ry="3"/><path d="M4 6v12c0 1.7 3.6 3 8 3s8-1.3 8-3V6M4 12c0 1.7 3.6 3 8 3s8-1.3 8-3"/></svg>Directory</div>
    <div class="nav-item abs" style="top:795px"><svg width="24" height="24" viewBox="0 0 24 24" fill="none" stroke="#111" stroke-width="2"><rect x="4" y="3" width="16" height="18" rx="1"/><path d="M8 8h8M8 12h8M8 16h5"/></svg>Documents<svg class="chev" width="16" height="16" viewBox="0 0 16 16"><path d="M4 6l4 4 4-4" stroke="#111" stroke-width="2" fill="none"/></svg></div>
    <div class="nav-item abs" style="top:848px"><svg width="24" height="24" viewBox="0 0 24 24" fill="none" stroke="#111" stroke-width="2"><path d="M12 2l9 5v10l-9 5-9-5V7z"/><path d="M3 7l9 5 9-5M12 12v10"/></svg>Packages</div>

    <div class="nav-label abs" style="top:922px">SETTINGS &amp; SUPPORT</div>
    <div class="nav-item abs" style="top:949px"><svg width="24" height="24" viewBox="0 0 24 24" fill="none" stroke="#111" stroke-width="2"><circle cx="12" cy="12" r="3"/><path d="M12 2v3M12 19v3M2 12h3M19 12h3M5 5l2 2M17 17l2 2M5 19l2-2M17 7l2-2"/><circle cx="12" cy="12" r="7"/></svg>Settings<svg class="chev" width="16" height="16" viewBox="0 0 16 16"><path d="M4 6l4 4 4-4" stroke="#111" stroke-width="2" fill="none"/></svg></div>
    <div class="nav-item abs" style="top:1002px"><svg width="24" height="24" viewBox="0 0 24 24" fill="none" stroke="#111" stroke-width="2"><path d="M4 15v-3a8 8 0 0116 0v3"/><rect x="3" y="14" width="4" height="6" rx="1"/><rect x="17" y="14" width="4" height="6" rx="1"/></svg>Tickets<span class="badge">1</span></div>

    <div class="logout abs"><svg width="26" height="26" viewBox="0 0 24 24" fill="none" stroke="#111" stroke-width="2"><path d="M10 4H4v16h6M14 8l4 4-4 4M18 12H9"/></svg>Logout<span class="go"><svg width="12" height="12" viewBox="0 0 12 12"><path d="M4 2l4 4-4 4" stroke="#111" stroke-width="1.8" fill="none"/></svg></span></div>
  </aside>

  <header class="topbar abs">
    <div class="back-btn abs"><svg width="22" height="22" viewBox="0 0 22 22"><path d="M18 11H4M10 5l-6 6 6 6" stroke="#111" stroke-width="2.2" fill="none" stroke-linecap="round"/></svg>Back</div>
    <nav class="crumbs abs"><span>Dashboard</span><svg width="10" height="12" viewBox="0 0 10 12"><path d="M3 2l4 4-4 4" stroke="#666" stroke-width="1.6" fill="none"/></svg><span>Overview</span><svg width="10" height="12" viewBox="0 0 10 12"><path d="M3 2l4 4-4 4" stroke="#666" stroke-width="1.6" fill="none"/></svg><span class="here">Home</span></nav>
    <div class="bell-btn abs"><svg width="26" height="26" viewBox="0 0 24 24" fill="none" stroke="#111" stroke-width="2"><path d="M6 17V11a6 6 0 0112 0v6l2 2H4z"/><path d="M10 21h4"/><circle cx="18" cy="5" r="3" fill="#e53935" stroke="none"/></svg></div>
    <div class="avatar abs" role="img" aria-label="Profile photo of the signed-in user"></div>
    <div class="user-name abs">Clara Whitmore</div>
    <div class="user-role abs">Development Manager</div>
    <svg class="user-chev abs" width="16" height="16" viewBox="0 0 16 16"><path d="M4 6l4 4 4-4" stroke="#111" stroke-width="2" fill="none"/></svg>
  </header>

  <main class="main abs">
    <h1 class="title abs">Overview</h1>
    <p class="desc abs">Property details, compliance items, and financial responsibilities, offering quick access to service charge schedules, occupant invitations, and payment setup.</p>
    <div class="report-btn abs">+ Make Report</div>
    <div class="updated abs">Last updated: 27 December 2024 09:37</div>

    <section class="setup abs">
      <h2>Please complete basic setup</h2>
      <div class="setup-row" style="top:67px"><span class="dot"></span>Service Charge Schedules<span class="btn">Set Up <svg width="10" height="12" viewBox="0 0 10 12"><path d="M3 2l4 4-4 4" stroke="#111" stroke-width="1.8" fill="none"/></svg></span></div>
      <div class="setup-row" style="top:120px"><span class="dot"></span>Service Charge Apportionment<span class="btn">Set Up <svg width="10" height="12" viewBox="0 0 10 12"><path d="M3 2l4 4-4 4" stroke="#111" stroke-width="1.8" fill="none"/></svg></span></div>
      <div class="setup-row" style="top:173px"><span class="dot"></span>Invite Residents &amp; Leaseholders<span class="btn">Set Up <svg width="10" height="12" viewBox="0 0 10 12"><path d="M3 2l4 4-4 4" stroke="#111" stroke-width="1.8" fill="none"/></svg></span></div>
      <div class="setup-row" style="top:226px"><span class="dot"></span>Connect Payment Provider<span class="btn">Set Up <svg width="10" height="12" viewBox="0 0 10 12"><path d="M3 2l4 4-4 4" stroke="#111" stroke-width="1.8" fill="none"/></svg></span></div>
    </section>

    <div class="divider abs"></div>
    <div class="tabs abs"><div class="tab on">Summary</div><div class="tab off">Details</div></div>

    <h3 class="section-h abs" style="top:663px">General</h3>
    <div class="table abs">
      <div class="trow" style="top:0"><span class="k">Units</span><span class="v">85</span><span class="go"><svg width="12" height="14" viewBox="0 0 12 14"><path d="M4 2l5 5-5 5" stroke="#111" stroke-width="2" fill="none"/></svg></span></div>
      <div class="trow" style="top:82px"><span class="k">Handover Date</span><span class="v">12 January 2023</span><span class="go"><svg width="12" height="14" viewBox="0 0 12 14"><path d="M4 2l5 5-5 5" stroke="#111" stroke-width="2" fill="none"/></svg></span></div>
      <div class="trow" style="top:164px"><span class="k">Address</span><span class="v">42 Linden Grove Terrace, London, N4 2QT</span><span class="go"><svg width="12" height="14" viewBox="0 0 12 14"><path d="M4 2l5 5-5 5" stroke="#111" stroke-width="2" fill="none"/></svg></span></div>
      <div class="trow" style="top:246px;border-bottom:none"><span class="k">Section 20 limit</span><span class="v">£20</span></div>
    </div>

    <h3 class="section-h abs" style="top:1073px">Compliance</h3>
    <div class="tile abs" style="left:19px;top:1122px"><span class="tag">Asbestos</span><div class="box">NA<div class="sub">-</div></div></div>
    <div class="tile warn abs" style="left:274px;top:1122px"><span class="tag">Legionellas</span><svg class="ico" width="26" height="26" viewBox="0 0 26 26" fill="none" stroke="#c2410c" stroke-width="2"><circle cx="13" cy="13" r="11"/><path d="M10 10a3 3 0 015 1c0 2-2 2-2 4"/><circle cx="13" cy="19" r=".8" fill="#c2410c"/></svg><div class="box">-<div class="sub">-</div></div></div>
    <div class="tile alert abs" style="left:530px;top:1122px"><span class="tag">Drains</span><svg class="ico" width="26" height="26" viewBox="0 0 26 26" fill="none" stroke="#c62828" stroke-width="2"><circle cx="13" cy="13" r="11"/><path d="M13 7v7"/><circle cx="13" cy="18.5" r=".8" fill="#c62828"/></svg><div class="box"><div class="first">Overdue</div><div class="sub">10 December 2023</div></div></div>
    <div class="tile abs" style="left:786px;top:1122px"><span class="tag">Gutters</span><div class="box">NA<div class="sub">-</div></div></div>
    <div class="tile abs" style="left:1041px;top:1122px"><span class="tag">Dry Risers</span><div class="box">NA<div class="sub">-</div></div></div>

    <h3 class="section-h abs" style="top:1294px">Insurances</h3>
    <div class="tile abs" style="left:19px;top:1343px"><span class="tag">Terrorism</span><div class="box">NA<div class="sub">-</div></div></div>
    <div class="tile abs" style="left:274px;top:1343px"><span class="tag">Buildings</span><div class="box">NA<div class="sub">-</div></div></div>
    <div class="tile abs" style="left:530px;top:1343px"><span class="tag">Engineering</span><div class="box">NA<div class="sub">-</div></div></div>
    <div class="tile abs" style="left:786px;top:1343px"><span class="tag">D &amp; O</span><div class="box">NA<div class="sub">-</div></div></div>
    <div class="tile abs" style="left:1041px;top:1343px"><span class="tag">Reinstatemen</span><div class="box">NA<div class="sub">-</div></div></div>

    <h3 class="section-h abs" style="top:1515px">Services Charge</h3>
    <div class="tile wide abs" style="left:19px;top:1563px"><span class="tag">Year End</span><div class="box">12/12/2024<div class="sub">-</div></div></div>
    <div class="tile wide abs" style="left:282px;top:1563px"><span class="tag">Demand Dates</span><div class="box">NA<div class="sub">-</div></div></div>

    <h3 class="section-h abs" style="top:1735px">Cosec</h3>
    <div class="tile wide abs" style="left:19px;top:1784px"><span class="tag">Are we responsible?</span><div class="box">No<div class="sub">-</div></div></div>
  </main>

</div>
</body>
</html>
```